Attractive WP design (Velmora) for our textile production and trading business

We need a design for our new website. We would like it to be based on the WP theme Velmora.

1) Description of the business
Kandrel GmbH is a textile company that is specialized in production and trading of high-quality cotton fabrics/products.

We…
• design and develop
• weave (incl. special weaving/embroidery technique)
• shear
• finish the products (Logo printing, packing)

Our products are…
• Swiss Ghutra
• Shemagh (=Yashmagh) (https://www.tervastoff.ch/en/competence/clothing-textiles/clothing-for-arab-and-african-markets/#210)
• Desdasha’s (https://www.tervastoff.ch/en/competence/clothing-textiles/clothing-for-arab-and-african-markets/#210)
• Emmas and Shawls
Emmas are traditional head coverings worn by Muslim man in Sudan. The cloth of exactly 5 yards in length is winded around the head like a turban. The cloth can be plain white, have a decorative trim or be colored. There are also matching scarfs.
• Brocade/Damask
• Atiku
• Kemora Voile (https://pomlatrade.com/products/kemora-3?_pos=2&_sid=98a067e86&_ss=r)
--> Please see attached pictures of the different fabrics and products

2) Target audience and users
• (Foreign) wholesalers interested in trading with Kandrel

3) Goals of the website
Kandrel has been a family-run textile business for 17 years with no web presence. The majority of our historical sales have been based on pre-existing relationships or word-of-mouth connections. Now, we seek to diversify our customer base. For this, we want our first website/online presence in order to:

• Enable foreign wholesalers to discover Kandrel as a supplier of Swiss quality fabric;
• Showcase both our current specific product line as well as our general manufacturing capabilities for new custom products;
• Enable inquiries/orders by interested parties

4) Design wishes
The design should reflect our high quality textiles. The design should be clean, inviting, friendly and professional. Colors can be chosen freely. Pictures should not overload sites but support our goal to attract and inspire future buyers.

If you have any questions, please reach out to us!

• the site will be multilingual (german/english/possibly french)

```html
<!DOCTYPE html>
<html lang="en">
<head>
<meta charset="utf-8">
<title>Kandrel GmbH – Swiss Textiles</title>
<link href="https://fonts.googleapis.com/css2?family=Poppins:wght@300;400;500;600;700&display=swap" rel="stylesheet">
<style>
:root{
  --ink:#1b1b1b;
  --text:#555;
  --muted:#777;
  --line:#e4e4e4;
  --field:#ececec;
  --footer:#f4f4f4;
  --teal:#06a5b1;
  --sky:#3bb4f8;
  --sun:#ffe600;
  --white:#fff;
}
*{box-sizing:border-box;margin:0;padding:0}
html,body{width:1200px;height:3297px;overflow:hidden}
body{position:relative;font-family:"Poppins",sans-serif;color:var(--ink);background:var(--white)}
.abs{position:absolute}
/* top bar */
.topbar{left:0;top:0;width:1200px;height:36px;border-bottom:1px solid var(--line);font-size:12px;color:var(--text)}
.topbar .contact{left:88px;top:10px;display:flex;gap:22px;align-items:center}
.topbar .contact span{display:flex;align-items:center;gap:6px}
.topbar .contact .sep{width:1px;height:16px;background:var(--line)}
.topbar .social{right:88px;top:11px;display:flex;gap:14px;align-items:center}
.dot{width:12px;height:12px;border-radius:50%;border:1.5px solid #666}
.vsep{width:1px;height:14px;background:var(--line)}
/* header */
.header{left:0;top:36px;width:1200px;height:96px}
.brand{font-weight:600;font-size:30px;letter-spacing:.5px;color:var(--ink)}
.header .brand{left:88px;top:26px}
.nav{left:419px;top:40px;display:flex;gap:32px;font-size:13px;font-weight:600;letter-spacing:.3px}
.search{left:791px;top:29px;width:222px;height:37px;background:var(--field);font-size:12px;color:#888;padding:11px 17px}
.search svg{position:absolute;right:14px;top:11px}
.lang{left:1046px;top:40px;display:flex;align-items:center;gap:6px;font-size:12px;font-weight:500}
.lang i{display:block;width:20px;height:20px;border-radius:50%;background:linear-gradient(#c8102e 50%,#2a3f8f 50%)}
/* hero */
.hero{left:0;top:132px;width:1200px;height:648px;background:linear-gradient(105deg,#d9d2c4 0%,#e0d9cc 40%,#c9bfae 60%,#3a3532 72%,#d6d1c8 85%,#e4dfd6 100%)}
.hero svg.blob{position:absolute;left:0;top:0}
.hero h1{position:absolute;left:116px;top:258px;font-weight:700;line-height:.95;color:var(--ink)}
.hero h1 .a{display:block;font-size:66px}
.hero h1 .b{display:block;font-size:94px}
.hero p{position:absolute;left:117px;top:410px;width:380px;font-size:15px;line-height:20px;color:#333}
.btn{display:inline-block;border:2px solid var(--ink);font-size:12px;font-weight:600;letter-spacing:.5px;text-align:center}
.hero .btn{position:absolute;left:117px;top:490px;width:153px;height:40px;line-height:36px}
/* section titles */
.title{left:0;width:1200px;text-align:center;font-weight:600;font-size:36px}
/* services */
.svc{font-size:16px;line-height:20px;color:#444}
.svc.left{text-align:right}
.svc-icon{width:40px;height:40px}
.big-brand{left:440px;top:990px;width:320px;text-align:center;font-size:72px;font-weight:600}
.rule{left:88px;top:1201px;width:1024px;height:1px;background:var(--line)}
/* products */
.ph{box-shadow:0 28px 40px rgba(0,0,0,.16)}
.prod h3{font-size:28px;font-weight:600;margin-bottom:10px}
.prod p{font-size:14.5px;line-height:20.5px;color:var(--muted);width:350px}
/* gallery */
.gallery{left:0;top:2581px;width:1200px;height:262px;display:flex}
.gallery div{flex:1}
/* footer */
.footer{left:0;top:2843px;width:1200px;height:454px;background:var(--footer)}
.footer .brand{font-size:48px}
.fsocial{display:flex;gap:9px}
.fsocial i{display:block;width:38px;height:38px;border-radius:50%;background:#e2e2e2}
.fcol h4{font-size:20px;font-weight:600;margin-bottom:18px}
.fcol li{list-style:none;display:flex;gap:12px;font-size:14px;color:var(--text);line-height:18px;margin-bottom:18px}
.fcol li svg{flex:none;margin-top:2px}
.vdiv{width:1px;background:#e0e0e0}
.news{font-size:14px;line-height:20px;color:var(--text);width:325px}
.email{width:320px;height:40px;background:#e9e9e9;font-size:12px;color:#666;padding:12px 20px;position:relative}
.email b{position:absolute;right:0;top:0;width:38px;height:40px;background:var(--ink)}
.copy{left:88px;top:3236px;width:1024px;border-top:1px solid #ddd;padding-top:22px;text-align:center;font-size:12px;font-weight:600}
.totop{left:1137px;top:3218px;width:36px;height:36px;border-radius:50%;background:var(--white);box-shadow:0 2px 8px rgba(0,0,0,.12)}
</style>
</head>
<body>

<div class="abs topbar">
  <div class="abs contact">
    <span><svg width="11" height="11" viewBox="0 0 24 24"><path d="M6.6 10.8a15 15 0 006.6 6.6l2.2-2.2c.3-.3.7-.4 1-.2 1.1.4 2.3.6 3.6.6.6 0 1 .4 1 1V20c0 .6-.4 1-1 1A17 17 0 013 4c0-.6.4-1 1-1h3.5c.6 0 1 .4 1 1 0 1.3.2 2.5.6 3.6.1.3 0 .7-.2 1z" fill="#555"/></svg>Telefon+41 55 618 27 09</span>
    <i class="sep"></i>
    <span><svg width="12" height="10" viewBox="0 0 24 18"><rect width="24" height="18" rx="2" fill="#555"/><path d="M1 2l11 8 11-8" stroke="#fff" stroke-width="2" fill="none"/></svg>E-Mail: hello@kandrel-textil.ch</span>
  </div>
  <div class="abs social" aria-label="Social links">
    <i class="dot"></i><i class="vsep"></i><i class="dot"></i><i class="vsep"></i><i class="dot"></i><i class="vsep"></i><i class="dot"></i>
  </div>
</div>

<header class="abs header">
  <div class="abs brand">Kandrel</div>
  <nav class="abs nav"><span>HOME</span><span>PRODUCTS</span><span>KANDREL GMBH</span><span>SHOP</span></nav>
  <div class="abs search">Search here...
    <svg width="15" height="15" viewBox="0 0 24 24"><circle cx="10" cy="10" r="7" stroke="#222" stroke-width="2.4" fill="none"/><path d="M15 15l6 6" stroke="#222" stroke-width="2.4"/></svg>
  </div>
  <div class="abs lang"><i></i>ENG <svg width="8" height="6" viewBox="0 0 8 6"><path d="M1 1l3 3 3-3" stroke="#222" stroke-width="1.5" fill="none"/></svg></div>
</header>

<section class="abs hero" role="img" aria-label="Photo of a man wearing a red and white checked shemagh in a bright room">
  <svg class="blob" width="1200" height="648" viewBox="0 0 1200 648"><path d="M0 214C120 140 250 92 371 92C500 92 580 180 569 300C555 440 480 560 422 648L0 648Z" fill="#fff"/></svg>
  <h1><span class="a">Kandrel</span><span class="b">GmbH</span></h1>
  <p>Kandrel GmbH is a textile company that is specialized in production and trading of high-quality cotton fabrics/products</p>
  <span class="btn">VIEW PRODUCTS</span>
</section>

<h2 class="abs title" style="top:865px">We Kandrel GmbH...</h2>

<div class="abs svc left" style="left:150px;top:958px;width:235px">We design and develop</div>
<svg class="abs svc-icon" style="left:400px;top:950px" viewBox="0 0 40 40" fill="none" stroke="#333" stroke-width="1.5"><rect x="4" y="14" width="22" height="22"/><path d="M10 20h10M10 26h10M10 32h6M20 6l14 14-8 8-14-14z"/></svg>
<div class="abs svc left" style="left:110px;top:1030px;width:275px">We weave (incl. special weaving/embroidery technique)</div>
<svg class="abs svc-icon" style="left:400px;top:1030px" viewBox="0 0 40 40" fill="none" stroke="#333" stroke-width="1.5"><circle cx="20" cy="21" r="16"/><circle cx="20" cy="21" r="9"/><circle cx="20" cy="21" r="3"/></svg>

<div class="abs big-brand">Kandrel</div>

<svg class="abs svc-icon" style="left:760px;top:950px" viewBox="0 0 40 40" fill="none" stroke="#333" stroke-width="1.5"><circle cx="9" cy="32" r="5"/><circle cx="31" cy="32" r="5"/><path d="M12 28L32 4M28 28L8 4"/></svg>
<div class="abs svc" style="left:813px;top:958px">We shear</div>
<svg class="abs svc-icon" style="left:760px;top:1028px" viewBox="0 0 40 40" fill="none" stroke="#333" stroke-width="1.5"><path d="M6 18l14-6 14 6v14l-14 6-14-6zM6 18l14 6 14-6M20 24v14M20 2v6M12 5l3 4M28 5l-3 4"/></svg>
<div class="abs svc" style="left:813px;top:1030px;width:260px">We finish the products (Logo printing, packing)</div>

<div class="abs rule"></div>

<h2 class="abs title" style="top:1280px">Our Products Are...</h2>

<div class="abs" style="left:130px;top:1523px;width:201px;height:168px;background:var(--teal)"></div>
<div class="abs ph" role="img" aria-label="Close-up of fine white cotton ghutra fabric with a woven label" style="left:188px;top:1362px;width:402px;height:268px;background:linear-gradient(150deg,#f1f1f1 0%,#cfcfcf 45%,#9a9a9a 75%,#111 92%)"></div>
<div class="abs prod" style="left:663px;top:1430px"><h3>Swiss Ghutra</h3><p>Morbi accumsan ipsum velit Nam nec tellus odio tincidunt auctor a ornare odio. Sed non mauris vitae erat consequat auctor eu in taciti sociosqu ad litora torquent per conubia...</p></div>

<div class="abs" style="left:868px;top:1839px;width:201px;height:168px;background:var(--sky)"></div>
<div class="abs ph" role="img" aria-label="Man wearing a red and white checked shemagh" style="left:607px;top:1686px;width:402px;height:267px;background:linear-gradient(100deg,#cfc6b6 0%,#b8a996 35%,#3d3833 55%,#d8d2c8 80%,#e8e3da 100%)"></div>
<div class="abs prod" style="left:138px;top:1774px"><h3>Shemagh (=Yashmagh)</h3><p>Morbi accumsan ipsum velit Nam nec tellus odio tincidunt auctor a ornare odio. Sed non mauris vitae erat consequat auctor eu in taciti sociosqu ad litora torquent per conubia...</p></div>

<div class="abs" style="left:130px;top:2172px;width:201px;height:168px;background:var(--sun)"></div>
<div class="abs ph" role="img" aria-label="Man wearing a red checked head scarf and white desdasha" style="left:188px;top:2018px;width:402px;height:268px;background:linear-gradient(120deg,#e8b89a 0%,#d9a888 40%,#c9a7a0 65%,#efe9e6 100%)"></div>
<div class="abs prod" style="left:663px;top:2086px"><h3>Desdasha’s</h3><p>Morbi accumsan ipsum velit Nam nec tellus odio tincidunt auctor a ornare odio. Sed non mauris vitae erat consequat auctor eu in taciti sociosqu ad litora torquent per conubia...</p></div>

<span class="abs btn" style="left:517px;top:2384px;width:167px;height:40px;line-height:36px">VIEW ALL PRODUCTS</span>

<h2 class="abs title" style="top:2518px">#KandrelGmbH...</h2>

<div class="abs gallery">
  <div role="img" aria-label="Customers in traditional dress at a shop" style="background:linear-gradient(160deg,#6e6150,#b9ac96)"></div>
  <div role="img" aria-label="Man in white robe and embroidered cap in an office" style="background:linear-gradient(160deg,#a79a84,#e2ddd2)"></div>
  <div role="img" aria-label="Man in a pale mint kaftan" style="background:linear-gradient(160deg,#c8c1b8,#a9e0d6)"></div>
  <div role="img" aria-label="Two men standing together, one in a white robe" style="background:linear-gradient(160deg,#8d7f6d,#dcd5c8)"></div>
  <div role="img" aria-label="Man in a light blue robe and white cap" style="background:linear-gradient(160deg,#9a7f68,#c4d3e6)"></div>
  <div role="img" aria-label="Family celebration with colourful outfits" style="background:linear-gradient(160deg,#5f8fb4,#e27fb0)"></div>
</div>

<footer class="abs footer">
  <div class="abs brand" style="left:128px;top:112px;width:180px;text-align:center">Kandrel</div>
  <div class="abs fsocial" style="left:129px;top:250px" aria-label="Social links"><i></i><i></i><i></i><i></i></div>
  <div class="abs vdiv" style="left:377px;top:90px;height:200px"></div>
  <div class="abs fcol" style="left:435px;top:95px">
    <h4>Kandrel GmbH</h4>
    <ul>
      <li><svg width="10" height="13" viewBox="0 0 10 14"><path d="M5 0a5 5 0 015 5c0 4-5 9-5 9S0 9 0 5a5 5 0 015-5z" fill="#333"/><circle cx="5" cy="5" r="2" fill="#fff"/></svg><span>Lindenweg 14<br>CH – 9105 Harwil<br>Switzerland</span></li>
      <li><svg width="12" height="12" viewBox="0 0 24 24"><path d="M6.6 10.8a15 15 0 006.6 6.6l2.2-2.2c.3-.3.7-.4 1-.2 1.1.4 2.3.6 3.6.6.6 0 1 .4 1 1V20c0 .6-.4 1-1 1A17 17 0 013 4c0-.6.4-1 1-1h3.5c.6 0 1 .4 1 1 0 1.3.2 2.5.6 3.6.1.3 0 .7-.2 1z" fill="#333"/></svg><span>Telefon+41 55 618 27 09</span></li>
      <li><svg width="13" height="10" viewBox="0 0 24 18"><rect width="24" height="18" rx="2" fill="#333"/><path d="M1 2l11 8 11-8" stroke="#fff" stroke-width="2" fill="none"/></svg><span>E-Mail: hello@kandrel-textil.ch</span></li>
      <li><svg width="12" height="12" viewBox="0 0 24 24" fill="none" stroke="#333" stroke-width="2.4"><circle cx="12" cy="12" r="10"/><path d="M2 12h20M12 2c3 3 3 17 0 20M12 2c-3 3-3 17 0 20"/></svg><span>CHE-482.319.706 MWST</span></li>
    </ul>
  </div>
  <div class="abs vdiv" style="left:688px;top:90px;height:200px"></div>
  <div class="abs fcol" style="left:745px;top:95px">
    <h4>Newsletter</h4>
    <p class="news">By subscribing to our mailing list you will always be updated with the latest news from us.</p>
    <div class="email" style="margin-top:22px">Enter email address<b><svg style="margin:12px 0 0 11px" width="16" height="16" viewBox="0 0 24 24"><path d="M2 11L22 2l-7 20-3-8z" fill="#fff"/></svg></b></div>
  </div>
</footer>
<div class="abs copy">© COPYRIGHT 2021 KANDREL GMBH, ALL RIGHTS RESERVED</div>
<div class="abs totop"><svg style="margin:10px 0 0 13px" width="10" height="14" viewBox="0 0 10 14"><path d="M5 13V1M1 5l4-4 4 4" stroke="#222" stroke-width="1.4" fill="none"/></svg></div>

</body>
</html>
```